Home Loan Introducer needs logo/business cards

We need a simple but classy logo for business cards and flyers. The business is a home loan referral business that is called an Introducer. The business name is "The Wayfarer".
I was thinking very simple and straight to the point on the front with "Home Loans" the only thing on the front with a nice background colour/s.
Then on the back, "The Wayfarer"
and "Quality Customer Service"
and "Email, text or call welcome"
and then my name, email address and phone number.
Updates
Thank you for all the designs :-)
Target Market(s)
Home buyers.
Home owners.
Investors.
Industry/Entity Type
Loan
Look and feel
Each slider illustrates characteristics of the customer's brand and the style your logo design should communicate.

```html
<!DOCTYPE html>
<html lang="en">
<head>
<meta charset="utf-8">
<title>The Wayfarer – Business Cards</title>
<link rel="stylesheet" href="https://fonts.googleapis.com/css2?family=Didact+Gothic&family=Russo+One&display=swap">
<style>
  :root {
    --stage: #ece8e2;
    --card-black: #222222;
    --amber: #f9a925;
    --amber-light: #fbbd55;
    --royal-blue: #0b6bc6;
    --ink: #1a1a1a;
    --white: #ffffff;
  }
  * { box-sizing: border-box; margin: 0; padding: 0; }
  html, body {
    width: 1200px; height: 750px; overflow: hidden;
    background: var(--stage);
  }
  .stage {
    position: relative; width: 1200px; height: 750px;
  }
  .card {
    position: absolute; top: 225px;
    width: 520px; height: 300px;
    background: var(--card-black);
    overflow: hidden;
    box-shadow: 0 6px 18px rgba(0,0,0,0.25);
  }

  /* Back card */
  .card--back { left: 50px; }
  .back__panel {
    position: absolute; top: 0; right: 0; bottom: 0; width: 272px;
    background: linear-gradient(160deg, var(--amber-light) 0%, var(--amber) 60%);
  }
  .back__band {
    position: absolute; left: 0; right: 0; height: 12px;
    background: var(--royal-blue);
  }
  .back__band--top { top: 48px; }
  .back__band--bottom { top: 236px; }

  .brand {
    position: absolute; left: 40px; top: 134px;
    display: flex; align-items: center; gap: 10px;
  }
  .brand__dot {
    width: 26px; height: 26px; border-radius: 50%;
    background: var(--royal-blue);
  }
  .brand__name {
    font-family: "Russo One", sans-serif;
    font-size: 20px; color: var(--amber);
    letter-spacing: 0.5px;
  }

  .details {
    position: absolute; left: 268px; top: 74px; width: 236px;
    font-family: "Didact Gothic", sans-serif;
    color: var(--white);
  }
  .details__perk {
    display: flex; align-items: center; gap: 6px;
    font-size: 13px; line-height: 20px;
  }
  .details__perk svg { flex: none; }
  .details__title {
    margin-top: 4px; padding-bottom: 3px;
    font-size: 17px; color: var(--royal-blue);
    border-bottom: 2px dotted var(--royal-blue);
  }
  .details__name {
    margin-top: 6px; font-size: 16px; color: var(--ink);
  }
  .details__contact {
    font-size: 12px; line-height: 16px; color: var(--ink);
  }

  /* Front card */
  .card--front { left: 630px; }
  .front__strip {
    position: absolute; left: 0; right: 0; top: 108px; height: 96px;
    background: var(--amber);
    border-top: 5px solid var(--white);
    border-bottom: 5px solid var(--white);
    border-radius: 0 10px 10px 0;
    display: flex; align-items: center; justify-content: center;
  }
  .front__title {
    font-family: "Russo One", sans-serif;
    font-size: 50px; color: var(--white);
    letter-spacing: 1px;
  }
</style>
</head>
<body>
<main class="stage">

  <section class="card card--back" aria-label="Business card, back">
    <div class="back__panel"></div>
    <div class="back__band back__band--top"></div>
    <div class="back__band back__band--bottom"></div>

    <div class="brand">
      <span class="brand__dot"></span>
      <span class="brand__name">THE WAYFARER</span>
    </div>

    <div class="details">
      <p class="details__perk">
        <svg width="12" height="12" viewBox="0 0 12 12" aria-hidden="true"><path d="M1 6.5 L4.5 10 L11 1.5" fill="none" stroke="#1a1a1a" stroke-width="2"/></svg>
        Quality Customer Service
      </p>
      <p class="details__perk">
        <svg width="12" height="12" viewBox="0 0 12 12" aria-hidden="true"><path d="M1 6.5 L4.5 10 L11 1.5" fill="none" stroke="#1a1a1a" stroke-width="2"/></svg>
        Email, text or call are Welcome
      </p>
      <p class="details__title">The Wayfarer</p>
      <p class="details__name">Daniel Morrow</p>
      <p class="details__contact">thewayfarer@postmail.net</p>
      <p class="details__contact">+639170482615</p>
    </div>
  </section>

  <section class="card card--front" aria-label="Business card, front">
    <div class="front__strip">
      <h1 class="front__title">HOME LOAN</h1>
    </div>
  </section>

</main>
</body>
</html>
```